Resume/CV/Cover Letter templates

We are a career management business and are starting to offer tailored career documents. we want 3-4 styles/themes with resume and cover letter templates. I have some examples to show you that are a good starting point (but are someone else's IP). see attached files

Target Market(s)

Corporate

Font styles to use
Sans Serif

Requirements
Must have
• Clean lines. Simple formatting. Corporate look and feel. Not too busy.
• Matching resume and cover letter documents
Nice to have
• One Blue theme
• One Green theme
• One other
Should not have
• too much jazziness!

```html
<!DOCTYPE html>
<html lang="en">
<head>
<meta charset="utf-8">
<title>Orange Resume and Cover Letter Templates</title>
<link rel="stylesheet" href="https://fonts.googleapis.com/css2?family=Montserrat:wght@700&family=Roboto+Condensed:wght@700&family=Open+Sans:wght@400;600;700&display=swap">
<style>
  :root {
    --orange: #f47c0f;
    --board: #363636;
    --paper: #ffffff;
    --ink: #222222;
    --body: #3c3c3c;
    --rule: #8c8c8c;
    --table-head: #8a8a8a;
  }
  * { box-sizing: border-box; margin: 0; padding: 0; }
  html, body { width: 1200px; height: 1200px; overflow: hidden; background: var(--board); }
  body { position: relative; font-family: "Open Sans", Arial, sans-serif; color: var(--body); }

  .sheet { position: absolute; width: 361px; height: 507px; background: var(--paper); overflow: hidden; box-shadow: 0 4px 10px rgba(0,0,0,.35); }
  .sheet--front { left: 194px; top: 27px; }
  .sheet--back { left: 638px; top: 27px; }
  .sheet--letter { left: 420px; top: 621px; }

  .label { position: absolute; font-family: "Open Sans", Arial, sans-serif; font-weight: 700; color: var(--orange); font-size: 27px; letter-spacing: .5px; transform: translateX(-50%); white-space: nowrap; }

  /* header */
  .header { position: absolute; left: 0; top: 0; width: 361px; height: 158px; background: var(--orange); border-bottom: 2px solid #d5d5d5; }
  .portrait-ring { position: absolute; width: 108px; height: 108px; border-radius: 50%; border: 1.5px solid #fff; }
  .portrait { position: absolute; left: 6px; top: 6px; width: 93px; height: 93px; border-radius: 50%; background: radial-gradient(circle at 50% 40%, #c9b7ab 0%, #8c7468 45%, #2a3a6a 75%, #213060 100%); border: 2px solid #fff; }
  .header .portrait-ring { left: 33px; top: 24px; }
  .name { position: absolute; font-family: "Montserrat", Arial, sans-serif; font-weight: 700; color: #fff; font-size: 16.8px; letter-spacing: .3px; white-space: nowrap; }
  .contact { position: absolute; font-size: 7px; line-height: 10px; color: #fff; }
  .contact dt { position: absolute; left: 0; }
  .contact dd { margin-left: 46px; }
  .contact-rule { position: absolute; height: 1px; background: #fff; }

  .bottom-bar { position: absolute; left: 0; bottom: 0; width: 361px; height: 10px; background: var(--orange); }

  /* sections */
  .heading { position: absolute; font-family: "Roboto Condensed", Arial, sans-serif; font-weight: 700; font-size: 9.5px; color: var(--ink); border-bottom: 2px solid var(--rule); padding-bottom: 1px; line-height: 11px; }
  .text { position: absolute; font-size: 4.9px; line-height: 7px; color: var(--body); text-align: justify; }
  .text--wide { font-size: 5.4px; }
  .sub { position: absolute; font-size: 6px; font-weight: 600; color: var(--orange); line-height: 7px; }
  .date { position: absolute; font-size: 4.9px; font-weight: 600; color: var(--body); }
  .caps { font-weight: 700; font-size: 4.6px; color: var(--ink); }
  .bullets { list-style: none; }
  .bullets li { position: relative; padding-left: 6px; }
  .bullets li::before { content: ""; position: absolute; left: 0; top: 2.2px; width: 3px; height: 3px; border-radius: 50%; background: var(--orange); }

  /* table */
  .summary { position: absolute; left: 150px; top: 188px; width: 194px; border-collapse: collapse; font-size: 4.6px; }
  .summary th { background: var(--table-head); color: #fff; font-weight: 700; height: 8px; padding: 0 2px; }
  .summary td { height: 8.8px; padding: 0 2px; color: var(--body); white-space: nowrap; }

  .hobby { position: absolute; top: 475px; width: 11px; height: 11px; background: var(--orange); border-radius: 50%; }

  /* letter */
  .letter-top { position: absolute; left: 0; top: 0; width: 361px; height: 10px; background: var(--orange); }
  .letter-rule { position: absolute; left: 0; top: 131px; width: 361px; height: 1.5px; background: #bdbdbd; }
  .sheet--letter .portrait-ring { left: 47px; top: 28px; width: 82px; height: 82px; border: 1.5px solid var(--orange); }
  .sheet--letter .portrait { left: 3.5px; top: 3.5px; width: 72px; height: 72px; border: 1.5px solid #fff; }
  .letter-name { position: absolute; left: 181px; top: 36px; font-family: "Montserrat", Arial, sans-serif; font-weight: 700; font-size: 9.3px; color: var(--ink); letter-spacing: .3px; white-space: nowrap; }
  .sheet--letter .contact { color: var(--ink); font-size: 5.6px; line-height: 8.3px; }
  .sheet--letter .contact dd { margin-left: 37px; }
  .sheet--letter .contact-rule { background: var(--orange); }
  .letter-text { font-size: 4.6px; line-height: 7.1px; }
  .letter-link { position: absolute; left: 35px; font-size: 5.6px; font-weight: 700; color: var(--orange); }
</style>
</head>
<body>

<!-- Resume front -->
<section class="sheet sheet--front">
  <header class="header">
    <div class="portrait-ring"><div class="portrait" role="img" aria-label="Portrait photo of the candidate"></div></div>
    <div class="name" style="left:167px;top:38px">NAME SERNAME</div>
    <dl class="contact" style="left:167px;top:63px;width:150px">
      <dt>Address:</dt><dd>102, Duis ut diam quam nulla<br>porttitor massa</dd>
    </dl>
    <div class="contact-rule" style="left:167px;top:89px;width:146px"></div>
    <dl class="contact" style="left:167px;top:97px;width:150px">
      <dt>Email:</dt><dd>info@samplefolio.com</dd>
      <dt style="top:10px">Phone:</dt><dd>55-0192-4738</dd>
      <dt style="top:20px">Portfolio:</dt><dd>www.samplefolio.com</dd>
    </dl>
  </header>

  <h2 class="heading" style="left:18px;top:174px;width:108px">CAREER PROFILE</h2>
  <p class="text" style="left:26px;top:191px;width:92px">Lorem ipsum dolor sit amet, consectetur adipiscing elit, sed do eiusmod tempor incididunt ut labore et dolore magna aliqua. Imperdiet dui accumsan sit amet. Vitae congue mauris rhoncus aenean vel elit scelerisque mauris pellentesque. Aliquet eget sit amet tellus cras adipiscing enim. Urna duis convallis convallis tellus id interdum.</p>

  <h2 class="heading" style="left:18px;top:275px;width:108px">KEY SKILLS</h2>
  <ul class="text text--wide bullets" style="left:24px;top:293px;width:94px">
    <li>Commercial Acumen – applies sound commercial knowledge to deliver robust market analysis; accurately identifying risk and opportunity to inform strategic planning and to enable effective negotiation, management and review of contracts.</li>
    <li style="margin-top:2px">[Skill]</li>
    <li>[Skill]</li>
    <li>[Skill]</li>
    <li>[Skill]</li>
  </ul>

  <h2 class="heading" style="left:18px;top:392px;width:108px">PERFORMANE</h2>
  <p class="text text--wide" style="left:24px;top:411px;width:94px">Euismod elementum nisi quis eleifend quam. Cursus euismod quis viverra nibh cras pulvinar mattis nunc. Habitasse platea dictumst vestibulum rhoncus est.</p>
  <p class="text text--wide" style="left:24px;top:450px;width:94px">Euismod elementum nisi quis eleifend quam. Cursus euismod quis viverra nibh cras pulvinar mattis nunc. Habitasse platea dictumst vestibulum rhoncus est.</p>

  <h2 class="heading" style="left:150px;top:174px;width:194px">EDUCATION</h2>
  <div class="sub" style="left:157px;top:198px">Vitae congue</div><div class="date" style="left:169px;top:207px">2005-2010</div>
  <p class="text" style="left:208px;top:199px;width:132px">Praesent elementum facilisis leo vel fringilla est. Vel fringilla est ullamcorper eget. Duis ut diam quam nulla porttitor massa. Euismod elementum nisi quis eleifend quam.</p>
  <div class="sub" style="left:157px;top:236px">Vitae congue</div><div class="date" style="left:169px;top:245px">2010-2012</div>
  <p class="text" style="left:208px;top:237px;width:132px">Praesent elementum facilisis leo vel fringilla est. Vel fringilla est ullamcorper eget. Duis ut diam quam nulla porttitor massa.</p>
  <div class="sub" style="left:157px;top:266px">Vitae congue</div><div class="date" style="left:169px;top:275px">2010-2012</div>
  <p class="text" style="left:208px;top:267px;width:132px">Praesent elementum facilisis leo vel fringilla est. Vel fringilla est ullamcorper eget. Duis ut diam quam nulla porttitor massa.</p>
  <div class="sub" style="left:157px;top:296px">Vitae congue</div><div class="date" style="left:169px;top:305px">2012-2016</div>
  <p class="text" style="left:208px;top:297px;width:132px">Praesent elementum facilisis leo vel fringilla est. Vel fringilla est ullamcorper eget. Duis ut diam quam nulla porttitor massa. Euismod elementum nisi quis eleifend quam.</p>

  <h2 class="heading" style="left:150px;top:366px;width:194px">LEADERSHIP ATTRIBUTES</h2>
  <div class="sub" style="left:157px;top:387px">Viverra nibh</div>
  <p class="text" style="left:157px;top:395px;width:184px">Praesent elementum facilisis leo vel fringilla est. Vel fringilla est ullamcorper eget. Duis ut diam quam nulla porttitor massa. Euismod elementum nisi quis eleifend quam.</p>
  <div class="sub" style="left:157px;top:422px">Viverra nibh</div>
  <p class="text" style="left:157px;top:430px;width:184px">Praesent elementum facilisis leo vel fringilla est. Vel fringilla est ullamcorper eget. Duis ut diam quam nulla porttitor massa. Euismod elementum nisi quis eleifend quam.</p>
  <div class="sub" style="left:157px;top:457px">Viverra nibh</div>
  <p class="text" style="left:157px;top:465px;width:184px">Praesent elementum facilisis leo vel fringilla est. Vel fringilla est ullamcorper eget. Duis ut diam quam nulla porttitor massa. Euismod elementum nisi quis eleifend quam.</p>

  <div class="bottom-bar"></div>
</section>

<!-- Resume back -->
<section class="sheet sheet--back">
  <header class="header">
    <div class="portrait-ring"><div class="portrait" role="img" aria-label="Portrait photo of the candidate"></div></div>
    <div class="name" style="left:167px;top:38px">NAME SERNAME</div>
    <dl class="contact" style="left:167px;top:63px;width:150px">
      <dt>Address:</dt><dd>102, Duis ut diam quam nulla<br>porttitor massa</dd>
    </dl>
    <div class="contact-rule" style="left:167px;top:89px;width:146px"></div>
    <dl class="contact" style="left:167px;top:97px;width:150px">
      <dt>Email:</dt><dd>info@samplefolio.com</dd>
      <dt style="top:10px">Phone:</dt><dd>55-0192-4738</dd>
      <dt style="top:20px">Portfolio:</dt><dd>www.samplefolio.com</dd>
    </dl>
  </header>

  <h2 class="heading" style="left:18px;top:163px;width:125px">EMPLOYMENT HISTORY</h2>
  <div class="sub" style="left:26px;top:185px;width:80px">HABITASSE PLATEA DICTUMST</div>
  <div class="text" style="left:26px;top:201px;width:92px">
    <p>Lorem ipsum dolor sit amet, consectetur adipiscing elit, sed do eiusmod tempor incididunt ut labore et dolore magna aliqua.</p>
    <p class="caps" style="margin-top:3px">RESPONSIBILITIES</p>
    <p>Imperdiet dui accumsan sit amet. Vitae congue mauris rhoncus.</p>
    <p class="caps" style="margin-top:3px">ACHIEVEMENTS</p>
    <p>Imperdiet dui accumsan sit amet. Vitae congue mauris rhoncus.</p>
  </div>
  <div class="sub" style="left:26px;top:296px;width:80px">HABITASSE PLATEA DICTUMST</div>
  <div class="text" style="left:26px;top:312px;width:92px">
    <p>Lorem ipsum dolor sit amet, consectetur adipiscing elit, sed do eiusmod tempor incididunt.</p>
    <p class="caps" style="margin-top:3px">RESPONSIBILITIES</p>
    <p>Imperdiet dui accumsan sit amet. Vitae congue mauris rhoncus.</p>
    <p class="caps" style="margin-top:3px">ACHIEVEMENTS</p>
    <p>Imperdiet dui accumsan sit amet. Vitae congue mauris rhoncus.</p>
  </div>
  <div class="sub" style="left:26px;top:391px;width:80px">HABITASSE PLATEA DICTUMST</div>
  <div class="text" style="left:26px;top:407px;width:92px">
    <p>Lorem ipsum dolor sit amet, consectetur adipiscing elit, sed do eiusmod tempor incididunt ut labore et dolore magna aliqua. Imperdiet dui accumsan sit amet.</p>
    <p class="caps" style="margin-top:3px">CHALLENGE &amp; CONTEXT</p>
    <p>Imperdiet dui accumsan sit amet. Vitae congue mauris rhoncus.</p>
    <p class="caps" style="margin-top:3px">RESULT</p>
    <p>Imperdiet dui accumsan sit amet. Vitae congue mauris rhoncus.</p>
  </div>

  <h2 class="heading" style="left:150px;top:163px;width:194px">CAREER SUMMARY</h2>
  <table class="summary">
    <thead><tr><th>DATES</th><th>POSITION/ORGANISATION</th><th>FOCUS &amp; RESULTS</th></tr></thead>
    <tbody>
      <tr><td>[Date] to [Date]</td><td>Lorem ipsum dolor sit amet</td><td>consectetur adipiscing</td></tr>
      <tr><td>[Date] to [Date]</td><td>Lorem ipsum dolor sit amet</td><td>consectetur adipiscing</td></tr>
      <tr><td>[Date] to [Date]</td><td>Lorem ipsum dolor sit amet</td><td>consectetur adipiscing</td></tr>
      <tr><td>[Date] to [Date]</td><td>Lorem ipsum dolor sit amet</td><td>consectetur adipiscing</td></tr>
      <tr><td>[Date] to [Date]</td><td>Lorem ipsum dolor sit amet</td><td>consectetur adipiscing</td></tr>
      <tr><td>[Date] to [Date]</td><td>Lorem ipsum dolor sit amet</td><td>consectetur adipiscing</td></tr>
      <tr><td>[Date] to [Date]</td><td>Lorem ipsum dolor sit amet</td><td>consectetur adipiscing</td></tr>
    </tbody>
  </table>

  <h2 class="heading" style="left:150px;top:274px;width:194px">PROFESSIONAL MEMBERSHIPS</h2>
  <div class="sub" style="left:157px;top:296px">Cursus euismod quis viverra</div>
  <p class="text" style="left:157px;top:304px;width:184px">Praesent elementum facilisis leo vel fringilla est. Vel fringilla est ullamcorper eget. Duis ut diam quam nulla porttitor massa. Euismod elementum nisi quis eleifend quam.</p>
  <div class="sub" style="left:157px;top:334px">Cursus euismod quis viverra</div>
  <p class="text" style="left:157px;top:342px;width:184px">Praesent elementum facilisis leo vel fringilla est. Vel fringilla est ullamcorper eget. Duis ut diam quam nulla porttitor massa. Euismod elementum nisi quis eleifend quam.</p>
  <div class="sub" style="left:157px;top:371px">Cursus euismod quis viverra</div>
  <p class="text" style="left:157px;top:379px;width:184px">Praesent elementum facilisis leo vel fringilla est. Vel fringilla est ullamcorper eget. Duis ut diam quam nulla porttitor massa. Euismod elementum nisi quis eleifend quam.</p>
  <div class="sub" style="left:157px;top:407px">Cursus euismod quis viverra</div>
  <p class="text" style="left:157px;top:415px;width:184px">Praesent elementum facilisis leo vel fringilla est. Vel fringilla est ullamcorper eget. Duis ut diam quam nulla porttitor massa. Euismod elementum nisi quis eleifend quam.</p>

  <h2 class="heading" style="left:150px;top:450px;width:194px">HOBBY</h2>
  <div class="hobby" style="left:165px" role="img" aria-label="Swimming icon"></div>
  <div class="hobby" style="left:199px" role="img" aria-label="Running icon"></div>
  <div class="hobby" style="left:228px" role="img" aria-label="Meditation icon"></div>
  <div class="hobby" style="left:254px" role="img" aria-label="Writing icon"></div>

  <div class="bottom-bar"></div>
</section>

<!-- Cover letter -->
<section class="sheet sheet--letter">
  <div class="letter-top"></div>
  <div class="portrait-ring"><div class="portrait" role="img" aria-label="Portrait photo of the candidate"></div></div>
  <div class="letter-name">FRIST NAME LASTNAME</div>
  <dl class="contact" style="left:181px;top:52px;width:130px">
    <dt>Address:</dt><dd>102, Duis ut diam quam nulla<br>porttitor massa</dd>
  </dl>
  <div class="contact-rule" style="left:181px;top:71px;width:122px"></div>
  <dl class="contact" style="left:181px;top:78px;width:130px">
    <dt>Email:</dt><dd>info@samplefolio.com</dd>
    <dt style="top:8.3px">Phone:</dt><dd>55-0192-4738</dd>
    <dt style="top:16.6px">Portfolio:</dt><dd>www.samplefolio.com</dd>
  </dl>
  <div class="letter-rule"></div>

  <div class="letter-link" style="top:174px">Dear [Name]</div>
  <div class="letter-link" style="top:186px">RE: [Subject]</div>
  <p class="text letter-text" style="left:35px;top:199px;width:290px">Lorem ipsum dolor sit amet, consectetur adipiscing elit, sed do eiusmod tempor incididunt ut labore et dolore magna aliqua. Ut enim ad minim veniam, quis nostrud exercitation ullamco laboris nisi ut aliquip ex ea commodo consequat. Duis aute irure dolor in reprehenderit in voluptate velit esse cillum dolore eu fugiat nulla pariatur. Excepteur sint occaecat cupidatat non proident, sunt in culpa qui officia deserunt mollit anim id est laborum.</p>
  <p class="text letter-text" style="left:35px;top:233px;width:290px">Lorem ipsum dolor sit amet, consectetur adipiscing elit, sed do eiusmod tempor incididunt ut labore et dolore magna aliqua. Ut enim ad minim veniam, quis nostrud exercitation ullamco laboris nisi ut aliquip ex ea commodo consequat. Duis aute irure dolor in reprehenderit in voluptate velit esse cillum dolore eu fugiat nulla pariatur. Excepteur sint occaecat cupidatat non proident, sunt in culpa qui officia deserunt mollit anim id est laborum.</p>
  <div class="letter-link" style="top:270px">[Skill] – [Description]</div>
  <div class="letter-link" style="top:283px">[Skill] – [Description]</div>
  <div class="letter-link" style="top:297px">[Skill] – [Description]</div>
  <div class="letter-link" style="top:310px">[Skill] – [Description]</div>
  <div class="letter-link" style="top:323px">[Skill] – [Description]</div>
  <p class="text letter-text" style="left:35px;top:337px;width:290px">Lorem ipsum dolor sit amet, consectetur adipiscing elit, sed do eiusmod tempor incididunt ut labore et dolore magna aliqua. Ut enim ad minim veniam, quis nostrud exercitation ullamco laboris nisi ut aliquip ex ea commodo consequat. Duis aute irure dolor in reprehenderit in voluptate velit esse cillum dolore eu fugiat nulla pariatur. Excepteur sint occaecat cupidatat non proident, sunt in culpa qui officia deserunt mollit anim id est laborum.</p>
  <div class="text letter-text" style="left:245px;top:383px;width:80px;text-align:right">Yours Sincerely,</div>
  <div class="letter-link" style="top:393px;left:299px">NAME</div>
  <div class="bottom-bar"></div>
</section>

<div class="label" style="left:376px;top:550px">FRONT</div>
<div class="label" style="left:817px;top:550px">BACK</div>
<div class="label" style="left:600px;top:1140px">COVER LATTER</div>

</body>
</html>
```